Product flyer with pricing

We manufacture iconic and luxury vending trailers. for our first trailer we need a flyer created to give to prospective clients with base pricing. I am uploading an example along with graphic files.

```html
<!DOCTYPE html>
<html lang="en">
<head>
<meta charset="utf-8">
<title>Meadow Cottage Mini – Vending House Flyer</title>
<link href="https://fonts.googleapis.com/css2?family=Exo+2:wght@300;400;600;700&family=Mukta:wght@300;400;600;700&display=swap" rel="stylesheet">
<style>
  :root{
    --green:#5db345;
    --green-light:#7dc242;
    --green-text:#8dc63f;
    --orange:#f7a823;
    --dark:#3b3b3d;
    --black:#111111;
    --ink:#1a1a1a;
    --grey-stripe:#d9d9d6;
    --white:#ffffff;
  }
  *{margin:0;padding:0;box-sizing:border-box}
  html,body{width:838px;height:1200px;overflow:hidden;background:var(--white)}
  .canvas{position:relative;width:838px;height:1200px;background:var(--white);font-family:"Mukta",sans-serif;color:var(--ink)}
  .flyer{position:absolute;left:34px;top:38px;width:776px;height:1092px;border:1px solid #444;overflow:hidden;background:var(--white)}
  .abs{position:absolute}

  /* header */
  .header-art{position:absolute;left:0;top:0;width:776px;height:343px}
  .brand{position:absolute;left:40px;top:92px;display:flex;align-items:center;gap:10px;font-family:"Exo 2",sans-serif;font-weight:700;font-size:25px;color:var(--green);letter-spacing:.5px}
  .brand-dot{width:22px;height:22px;border-radius:50%;background:var(--orange)}
  .title-block{position:absolute;left:40px;top:195px;color:var(--white);font-family:"Exo 2",sans-serif}
  .title-block .the,.title-block .name{font-weight:700;font-size:28px;line-height:34px}
  .title-block .rule{width:345px;height:1px;background:var(--white);margin:6px 0 8px}
  .title-block .tagline{font-weight:300;font-size:26px;line-height:30px}

  /* features */
  .features{position:absolute;left:29px;top:364px;width:285px}
  .features h2{font-size:18px;font-weight:700;margin-bottom:10px;line-height:22px}
  .features ul{list-style:none}
  .features li{position:relative;padding-left:26px;font-size:13.5px;line-height:17px;margin-bottom:19px}
  .features li svg{position:absolute;left:0;top:0;width:17px;height:15px}

  .gallery-bar{position:absolute;top:402px;width:16px;height:280px;background:var(--orange)}
  .thumb{position:absolute;width:197px;height:146px}
  .base-price{position:absolute;left:455px;top:693px;font-size:19px;font-weight:700}

  /* options band */
  .options{position:absolute;left:0;top:724px;width:776px;height:178px;background:linear-gradient(180deg,var(--green) 0%,var(--green-light) 100%);color:var(--white)}
  .option{position:absolute;font-family:"Exo 2",sans-serif;font-weight:700;font-size:17px;line-height:21px}
  .option .price{display:block;font-family:"Mukta",sans-serif;font-size:16px;line-height:20px;color:var(--ink)}
  .option .note{display:block;font-family:"Mukta",sans-serif;font-size:12px;line-height:13px;color:var(--white)}

  /* use cases */
  .uses{position:absolute;left:0;top:902px;width:776px;height:190px;background:var(--dark);color:var(--white)}
  .uses-tab{position:absolute;left:0;top:0;width:160px;height:28px}
  .uses-tab span{position:absolute;left:18px;top:3px;font-weight:700;font-size:16px}
  .use{position:absolute;font-size:13.5px;line-height:17px}
  .use h3{color:var(--green-text);font-size:15px;font-weight:700;line-height:19px}
  .contact{width:205px}
  .contact h3{color:var(--green-text);font-family:"Exo 2",sans-serif;font-size:16px;font-weight:700;line-height:20px}
  .contact .value{font-family:"Exo 2",sans-serif;font-weight:300;font-size:26px;line-height:32px;white-space:nowrap}
  .contact .value.email{font-size:20px}
</style>
</head>
<body>
<div class="canvas">
  <div class="flyer">
    <svg class="header-art" viewBox="0 0 776 343" aria-hidden="true">
      <polygon points="448,0 528,0 400,343 320,343" fill="var(--grey-stripe)"/>
      <polygon points="0,184 350,184 505,343 0,343" fill="var(--green)"/>
    </svg>
    <div class="abs" role="img" aria-label="Photo of the white board-and-batten vending house on a tandem trailer under blue sky"
         style="left:400px;top:0;width:376px;height:343px;background:linear-gradient(180deg,#5f93c9 0%,#dfe5ea 45%,#9a9a9c 85%,#5a5a5c 100%);clip-path:polygon(128px 0,376px 0,376px 343px,0 343px)"></div>

    <div class="brand"><span class="brand-dot"></span>BRIGHTNOOK BUILDS</div>

    <div class="title-block">
      <div class="the">The</div>
      <div class="name">“Meadow Cottage Mini”</div>
      <div class="rule"></div>
      <div class="tagline">Luxury, mobile vending house</div>
    </div>

    <section class="features">
      <h2>Base unit features:</h2>
      <ul>
        <li><svg viewBox="0 0 17 15"><path d="M1 8 L6 13 L16 1" fill="none" stroke="var(--green)" stroke-width="3"/></svg>Trailer features tandem wheels w/ brakes</li>
        <li><svg viewBox="0 0 17 15"><path d="M1 8 L6 13 L16 1" fill="none" stroke="var(--green)" stroke-width="3"/></svg>Steel frame construction for fire retardation safety and weight reduction.</li>
        <li><svg viewBox="0 0 17 15"><path d="M1 8 L6 13 L16 1" fill="none" stroke="var(--green)" stroke-width="3"/></svg>100% off grid with solar and lithium battery system allowing the trailer to be used in places not accessible by traditional trailers.</li>
        <li><svg viewBox="0 0 17 15"><path d="M1 8 L6 13 L16 1" fill="none" stroke="var(--green)" stroke-width="3"/></svg>80 gallon water supply tank</li>
        <li><svg viewBox="0 0 17 15"><path d="M1 8 L6 13 L16 1" fill="none" stroke="var(--green)" stroke-width="3"/></svg>100 gallon waste water tank</li>
        <li><svg viewBox="0 0 17 15"><path d="M1 8 L6 13 L16 1" fill="none" stroke="var(--green)" stroke-width="3"/></svg>Cupboards, cabinets &amp; four<br>stainless steel sinks.</li>
        <li><svg viewBox="0 0 17 15"><path d="M1 8 L6 13 L16 1" fill="none" stroke="var(--green)" stroke-width="3"/></svg>60” Gas shock serving window</li>
      </ul>
    </section>

    <div class="gallery-bar" style="left:331px"></div>
    <div class="gallery-bar" style="left:757px;width:19px"></div>
    <div class="thumb" role="img" aria-label="Side view of the vending house on its trailer" style="left:347px;top:371px;background:linear-gradient(180deg,#6f9fd0 0%,#e8ecef 50%,#7a7a7c 100%)"></div>
    <div class="thumb" role="img" aria-label="Vending house with the serving window raised" style="left:560px;top:371px;background:linear-gradient(180deg,#6f9fd0 0%,#e8ecef 50%,#7a7a7c 100%)"></div>
    <div class="thumb" role="img" aria-label="Angled view showing the serving window and awning" style="left:347px;top:536px;background:linear-gradient(180deg,#6f9fd0 0%,#e8ecef 50%,#7a7a7c 100%)"></div>
    <div class="thumb" role="img" aria-label="Rear view of the vending house" style="left:560px;top:536px;background:linear-gradient(180deg,#6f9fd0 0%,#e8ecef 50%,#7a7a7c 100%)"></div>

    <div class="base-price">Base price: $45,000</div>

    <section class="options">
      <div class="option" style="left:40px;top:22px">HVAC - Northwind Mini Split<span class="price">$1,800</span></div>
      <div class="option" style="left:289px;top:22px">Upper loft storage area<span class="price">$1,200</span></div>
      <div class="option" style="left:555px;top:22px">Ice machine<span class="price">$1,100</span></div>
      <div class="option" style="left:40px;top:92px">Cooler / Glass front<br>Commercial refrigerator<span class="price">$1,600</span></div>
      <div class="option" style="left:289px;top:92px">Signage and graphics<span class="price">$2,000 - $5,000</span><span class="note">depend on complexity</span></div>
      <div class="option" style="left:555px;top:92px">Other custom items<br>available on request.</div>
    </section>

    <section class="uses">
      <svg class="uses-tab" viewBox="0 0 160 28" aria-hidden="true"><polygon points="0,0 160,0 134,28 0,28" fill="var(--black)"/></svg>
      <div class="uses-tab"><span>Use cases:</span></div>

      <div class="use" style="left:40px;top:36px;width:240px"><h3>Food:</h3>Lemonade, Coffee, pizza, cookies, doughnuts, barbecue and more!</div>
      <div class="use" style="left:40px;top:110px;width:240px"><h3>Retail:</h3>Clothing, watches, jewelry,<br>flowers and more!</div>
      <div class="use" style="left:289px;top:36px;width:215px"><h3>Corporate:</h3>Product info, demonstration,<br>information, brand awareness.</div>
      <div class="use" style="left:289px;top:110px;width:250px"><h3>Fundraisers:</h3>Girls/boy sports, non profits, etc.</div>

      <div class="contact abs" style="left:555px;top:36px"><h3>CONTACT</h3><div class="value">0123456789</div></div>
      <div class="contact abs" style="left:555px;top:110px"><h3>EMAIL</h3><div class="value email">hi@brightnook.com</div></div>
    </section>
  </div>
</div>
</body>
</html>
```